Business Card Design Project

We are after a business card design for our construction company. Called R & T Belmore Construction Solutions. We build designer homes mainly one of's. We would like something with punch, eye catching like the homes we build, modern style maybe geometrical or slightly abstract. It is a long business name we realise but we wont mind if our name is more in the back ground making Construction Solutions the focus ??? Colours maybe purple and black ??? Don't really have any set colours.

Industry/Entity Type

Construction

Requirements
Must have
• Business name contact details and our personal names perhaps at bottom somewhere
Nice to have
• A business card which has a simple easily recognised symbol or logo on it

```html
<!DOCTYPE html>
<html lang="en">
<head>
<meta charset="utf-8">
<title>R &amp; T Belmore Construction Solutions – Business Cards</title>
<link rel="stylesheet" href="https://fonts.googleapis.com/css2?family=Questrial&display=swap">
<style>
  :root {
    --page: #ffffff;
    --card: #000000;
    --band: #404040;
    --violet: #8a1ee6;
    --violet-bright: #a52cf0;
    --magenta: #c020e0;
    --white: #ffffff;
    --caption: #111111;
    --sans: "Questrial", "Century Gothic", sans-serif;
  }
  * { margin: 0; padding: 0; box-sizing: border-box; }
  html, body { width: 1200px; height: 848px; overflow: hidden; background: var(--page); }
  body { position: relative; font-family: var(--sans); }

  .card { position: absolute; width: 462px; height: 263px; background: var(--card); overflow: hidden; color: var(--white); }
  .card--front-double { left: 135px; top: 118px; }
  .card--back-double  { left: 609px; top: 118px; }
  .card--single-centre { left: 135px; top: 453px; height: 264px; }
  .card--single-split  { left: 609px; top: 453px; height: 264px; }

  .band { position: absolute; left: 0; bottom: 0; width: 100%; height: 24px; background: var(--band);
          display: flex; align-items: center; justify-content: center; font-size: 11px; letter-spacing: 0.3px; }
  .band__accent { color: var(--violet-bright); margin-left: 4px; }

  .brand { position: absolute; text-align: center; color: var(--violet); }
  .brand__name { display: block; letter-spacing: 3px; line-height: 1; }
  .brand__tagline { display: block; line-height: 1; white-space: nowrap; }

  .card--front-double .brand { left: 0; width: 100%; top: 110px; }
  .card--front-double .brand__name { font-size: 30px; }
  .card--front-double .brand__tagline { font-size: 19px; margin-top: 36px; }

  .card--back-double .brand { left: 0; width: 100%; top: 72px; }
  .card--back-double .brand__name { font-size: 14px; letter-spacing: 2px; }
  .card--back-double .brand__tagline { font-size: 10px; margin-top: 13px; }

  .card--single-centre .brand { left: 0; width: 460px; top: 100px; }
  .card--single-centre .brand__name { font-size: 30px; }
  .card--single-centre .brand__tagline { font-size: 19px; margin-top: 36px; }

  .card--single-split .brand { left: 10px; width: 212px; top: 115px; }
  .card--single-split .brand__name { font-size: 24px; letter-spacing: 2px; }
  .card--single-split .brand__tagline { font-size: 19px; margin-top: 42px; }

  .glow-rule { position: absolute; height: 1px;
               background: linear-gradient(90deg, transparent, var(--violet) 50%, transparent); }
  .card--back-double .glow-rule { left: 30px; width: 402px; top: 141px; }
  .card--single-centre .glow-rule { left: 40px; width: 380px; top: 199px; }

  .contact { position: absolute; left: 0; width: 100%; text-align: center; font-size: 8px; line-height: 10px; }
  .card--back-double .contact { top: 157px; }
  .card--single-centre .contact { top: 217px; width: 452px; }
  .contact__name { color: var(--magenta); margin-right: 6px; }

  .divider { position: absolute; left: 231px; top: 18px; width: 1px; height: 246px;
             background: linear-gradient(180deg, transparent, var(--violet) 20%, var(--violet) 85%, transparent); }
  .person { position: absolute; left: 266px; top: 40px; }
  .person__name { font-size: 16px; color: var(--violet-bright); line-height: 18px; }
  .person__title { font-size: 10px; margin-top: 3px; }
  .details { position: absolute; right: 30px; text-align: right; font-size: 10px; line-height: 12.5px; }
  .details--address { top: 124px; }
  .details--reach { top: 172px; }

  .caption { position: absolute; font-size: 10px; color: var(--caption); text-align: center; width: 300px; }
  .caption--double { left: 453px; top: 401px; }
  .caption--single-a { left: 211px; top: 734px; }
  .caption--single-b { left: 688px; top: 734px; }
</style>
</head>
<body>

  <section class="card card--front-double" aria-label="Double sided card, front">
    <div class="brand">
      <span class="brand__name">R &amp; T BELMORE</span>
      <span class="brand__tagline">Construction Solutions</span>
    </div>
    <div class="band"></div>
  </section>

  <section class="card card--back-double" aria-label="Double sided card, back">
    <div class="brand">
      <span class="brand__name">R &amp; T BELMORE</span>
      <span class="brand__tagline">Construction Solutions</span>
    </div>
    <div class="glow-rule"></div>
    <div class="contact">
      <div><span class="contact__name">Your name here</span>Title here</div>
      <div>123 Anywhere st, Inanarea, Inatown, Near you</div>
      <div>Email: abcez@123&nbsp;&nbsp;&nbsp;Phone: 01 234 567</div>
    </div>
    <div class="band">INCORPORATING DEPENDABLE<span class="band__accent">CONSTRUCTION SOLUTIONS</span></div>
  </section>

  <p class="caption caption--double">Double sided business card</p>

  <section class="card card--single-centre" aria-label="Single sided card, centred layout">
    <div class="brand">
      <span class="brand__name">R &amp; T BELMORE</span>
      <span class="brand__tagline">Construction Solutions</span>
    </div>
    <div class="glow-rule"></div>
    <div class="contact">
      <div><span class="contact__name">Your name here</span>Title here</div>
      <div>123 Anywhere st, Inanarea, Inatown, Near you</div>
      <div>Email: abcez@123&nbsp;&nbsp;&nbsp;Phone: 01 234 567</div>
    </div>
  </section>

  <section class="card card--single-split" aria-label="Single sided card, split layout">
    <div class="brand">
      <span class="brand__name">R &amp; T BELMORE</span>
      <span class="brand__tagline">Construction Solutions</span>
    </div>
    <div class="divider"></div>
    <div class="person">
      <div class="person__name">Your name here</div>
      <div class="person__title">Title</div>
    </div>
    <div class="details details--address">
      <div>123 Anywhere st</div>
      <div>Inanarea Inatown</div>
      <div>Nearyou</div>
    </div>
    <div class="details details--reach">
      <div>Phone. 01 234 567</div>
      <div>Email. abcez@123.co.nz</div>
    </div>
  </section>

  <p class="caption caption--single-a">Single side business card</p>
  <p class="caption caption--single-b">Single side business card</p>

</body>
</html>
```